KORVAL Works Pty Ltd. Website and Domain

www.korvalworks.com.au

require email addresses setup.

Info@korvalworks.com.au
accounts@korvalworks.com.au
peter.gralow@korvalworks.com.au
lucas.brenner@korvalworks.com.au

Website should promote commercial and domestic electrical services, audio visual services and data and fibre installations.

similar to my mates site www.bryfield.com.au

Website needs to promote professionalism, electrical/electrician, audio visual and data/fibre cabling installations.

promote environmental friendly imaginary.

Coding

Coded - Design and coding required

```html
<!DOCTYPE html>
<html lang="en">
<head>
<meta charset="utf-8">
<title>KORVAL Works – Electrical, Audio Visual &amp; Data</title>
<link href="https://fonts.googleapis.com/css2?family=Lato:wght@400;700;900&display=swap" rel="stylesheet">
<style>
:root{
  --blue:#2a8fd0;
  --blue-dark:#1f7fc2;
  --green:#8dc63f;
  --ink:#1e1e1e;
  --text:#333;
  --grey-bg:#f2f2f2;
  --card-bg:#f3f3f3;
  --white:#fff;
}
*{box-sizing:border-box;margin:0;padding:0}
html,body{width:1200px;height:3588px;overflow:hidden;background:var(--white)}
body{font-family:'Lato',sans-serif;color:var(--text);position:relative}
.abs{position:absolute}
section,header,nav,footer{position:absolute;left:0;width:1200px}
.btn{position:absolute;display:flex;align-items:center;justify-content:center;border-radius:26px;
  background:linear-gradient(90deg,var(--blue),var(--green));color:#fff;font-weight:700;font-size:15px;letter-spacing:.3px}
h2.section-title{position:absolute;font-weight:900;font-size:33px;color:var(--ink);text-transform:uppercase;letter-spacing:-.3px}
p.body{font-size:15px;line-height:27px;color:#333}

/* header */
.site-header{top:0;height:113px;background:#fff}
.brand{left:75px;top:25px;display:flex;align-items:center;gap:10px}
.brand-dot{width:62px;height:62px;border-radius:50%;border:5px solid var(--green)}
.brand-name{font-size:42px;font-weight:700;color:var(--blue);letter-spacing:2px}
.call{left:885px;top:30px}
.call small{display:block;font-size:19px;font-weight:700;color:var(--ink)}
.call strong{display:block;font-size:34px;font-weight:700;color:var(--green);line-height:40px}

.main-nav{top:113px;height:54px;background:linear-gradient(90deg,#2d8ed2,#3a97d6)}
.main-nav ul{list-style:none;display:flex;position:absolute;left:188px;top:0;height:54px}
.main-nav li{height:54px;display:flex;align-items:center;padding:0 27px;color:#fff;font-size:15px;font-weight:700}
.main-nav li.active{background:var(--green);padding:0 30px}

/* hero */
.hero{top:167px;height:571px;overflow:hidden}
.hero-photo{position:absolute;inset:0;background:linear-gradient(90deg,#cbc6f3 0%,#c3c2f0 35%,#9fb4e6 55%,#7a8bb0 75%,#5b5a58 100%)}
.hero h1{position:absolute;left:73px;top:130px;font-size:64px;font-weight:900;color:var(--ink);letter-spacing:-1px}
.hero p{position:absolute;left:75px;top:207px;width:470px;font-size:21px;line-height:31px;color:#222}

/* welcome */
.welcome{top:738px;height:546px}
.welcome-art{position:absolute;left:75px;top:65px;width:511px;height:422px;border-radius:50%;
  background:radial-gradient(circle,#e4f1fa 0%,#eef6e2 70%,#fff 100%)}
.welcome h2{left:615px;top:122px;font-size:31px}
.welcome p{position:absolute;left:615px;top:178px;width:520px;font-size:14.5px;line-height:31.5px}

/* services */
.services{top:1284px;height:592px;background:var(--grey-bg)}
.services h2{left:74px;top:62px}
.services .intro{position:absolute;left:75px;top:115px;width:300px;font-size:14.5px;line-height:27px}
.hub{position:absolute;left:390px;top:178px;width:300px;height:300px;border-radius:50%;
  background:radial-gradient(circle,#dcebf6 0%,#e8f2da 75%,var(--grey-bg) 100%)}
.svc-icon{position:absolute;width:80px;height:80px;border-radius:50%;
  background:linear-gradient(135deg,#3aa0c8,#55b48a)}
.svc-icon svg{position:absolute;left:22px;top:22px}
.svc{position:absolute;width:270px}
.svc h3{font-size:21px;font-weight:700;color:var(--blue);margin-bottom:5px}
.svc p{font-size:14.5px;line-height:25px;color:#333}
.svc.right-align{text-align:right}

/* service cards */
.service-cards{top:1876px;height:444px;background:#fff}
.card{position:absolute;top:56px;width:511px;height:330px;border-radius:6px;overflow:hidden}
.card .photo{position:absolute;inset:0}
.card h3{position:absolute;left:0;right:0;top:120px;text-align:center;color:#fff;font-size:28px;font-weight:700;text-transform:uppercase}

/* clients */
.clients{top:2320px;height:263px;background:var(--grey-bg)}
.clients h2{left:0;width:1200px;text-align:center;top:45px;font-size:28px}
.client{position:absolute;top:119px;width:242px;height:83px;background:#fff;box-shadow:0 1px 4px rgba(0,0,0,.12);
  display:flex;align-items:center;justify-content:center;gap:10px;font-size:26px;font-weight:700;color:#333}
.client i{display:block;width:22px;height:22px;border-radius:50%;background:var(--blue)}

/* news & testimonials */
.news{top:2583px;height:506px;background:#fff}
.news h2{top:50px;font-size:31px}
.post{position:absolute;left:75px;width:600px;height:147px}
.post .thumb{position:absolute;left:0;top:0;width:241px;height:147px;border-radius:4px}
.post h3{position:absolute;left:267px;top:10px;font-size:20px;font-weight:700;color:var(--blue)}
.post p{position:absolute;left:267px;top:44px;width:330px;font-size:14.5px;line-height:25px}
.quote{position:absolute;left:706px;width:420px;height:148px;background:var(--card-bg);border-radius:6px}
.quote .avatar{position:absolute;left:21px;top:22px;width:101px;height:101px;border-radius:4px;background:linear-gradient(135deg,#d9d6d2,#8b7f78)}
.quote p{position:absolute;left:142px;top:20px;width:260px;font-size:14.5px;line-height:25px}
.quote cite{position:absolute;left:142px;top:104px;font-style:normal;font-weight:700;font-size:15px;color:var(--blue)}

/* cta */
.cta{top:3089px;height:225px;background:linear-gradient(100deg,#2a8fd0 0%,#4ea7a6 45%,#8dc63f 100%);color:#fff;text-align:center}
.cta h2{position:absolute;left:0;width:1200px;top:42px;font-size:33px;font-weight:700}
.cta .sub{position:absolute;left:0;width:1200px;top:95px;font-size:15px}
.cta .phone{position:absolute;left:418px;top:134px;font-size:23px;font-weight:700}
.cta .outline{position:absolute;left:607px;top:135px;width:175px;height:45px;border:2px solid #fff;border-radius:24px;
  display:flex;align-items:center;justify-content:center;font-size:14px;font-weight:700}

/* footer */
.site-footer{top:3314px;height:274px;background:#fff}
.footer-brand{left:75px;top:55px;display:flex;align-items:center;gap:8px}
.footer-brand .brand-dot{width:52px;height:52px;border-width:4px}
.footer-brand .brand-name{font-size:34px}
.copy{left:75px;top:140px;font-size:13px;line-height:22px;color:#222}
.social{left:75px;top:202px;display:flex;gap:20px}
.social span{display:block;width:18px;height:18px;border-radius:3px;background:#2b2b2b}
.fcol h4{font-size:15px;font-weight:700;color:var(--ink);margin-bottom:12px}
.fcol li{list-style:none;font-size:14px;line-height:28px;color:#222}
.fcol .two{display:grid;grid-template-columns:100px 100px}
.fcol .spaced li{line-height:35px}
.contact li{display:flex;gap:14px;line-height:27px}
.contact svg{margin-top:8px}
</style>
</head>
<body>

<header class="site-header">
  <div class="abs brand"><span class="brand-dot"></span><span class="brand-name">KORVAL</span></div>
  <div class="abs call"><small>CALL TODAY</small><strong>1-800-555-0148</strong></div>
</header>

<nav class="main-nav">
  <ul>
    <li class="active">HOME</li><li>ABOUT US</li><li>SERVICES</li><li>REVIEWS</li><li>BLOG</li><li>CLIENTS</li><li>CONTACT US</li>
  </ul>
</nav>

<section class="hero">
  <div class="hero-photo" role="img" aria-label="Open electrical switchboard beside an engineer in a hard hat and hi-vis vest reading plans"></div>
  <h1>KORVAL</h1>
  <p>We Serve commercial and domestic electrical services, audio visual services and data and fibre installations.</p>
  <div class="btn" style="left:75px;top:334px;width:178px;height:48px">READ MORE</div>
</section>

<section class="welcome">
  <div class="welcome-art" role="img" aria-label="Brand illustration"></div>
  <h2 class="section-title">Welcome to our website</h2>
  <p class="body">Duis gravida nibh ut mauris posuere fermentum uisque sed lorem convallis, malesuada mauris ut, lacinia diam. Integer ut lectus ut dui vehicula gravida. Morbi varius massa quis elit commodo, ut lacinia mauris condimentum. Cras viverra non nibh quis variusauris nec elementum libero. Sed in sem ac tortor congue sollicitudin.</p>
  <div class="btn" style="left:615px;top:373px;width:178px;height:47px">READ MORE</div>
</section>

<section class="services">
  <h2 class="section-title">Our services</h2>
  <p class="intro">Duis gravida nibh ut mauris posuere fermentum uisque sed lorem convallis, malesuada mauris ut, lacinia diamnteger ut lectus ut dui.</p>
  <div class="btn" style="left:76px;top:246px;width:178px;height:49px">READ MORE</div>
  <div class="hub" role="img" aria-label="Brand illustration"></div>

  <div class="svc-icon" style="left:496px;top:79px"><svg width="36" height="36" viewBox="0 0 36 36" fill="none" stroke="#fff" stroke-width="2"><path d="M20 3 11 20h8l-3 13 10-18h-8z"/></svg></div>
  <div class="svc" style="left:612px;top:70px"><h3>Electrical Services</h3><p>Duis gravida nibh ut mauris posuere fermentum uisque sed loremlissuada mauris ut, lacinia.</p></div>

  <div class="svc-icon" style="left:350px;top:1416px;top:416px"><svg width="36" height="36" viewBox="0 0 36 36" fill="none" stroke="#fff" stroke-width="2"><rect x="4" y="6" width="28" height="18" rx="2"/><path d="M15 11v8l7-4z"/><path d="M12 30h12"/></svg></div>
  <div class="svc right-align" style="left:60px;top:409px"><h3>Audio Visual Services</h3><p>Duis gravida nibh ut mauris posuere fermentum uisque sed loremlissuada mauris ut, lacinia.</p></div>

  <div class="svc-icon" style="left:773px;top:416px"><svg width="36" height="36" viewBox="0 0 36 36" fill="none" stroke="#fff" stroke-width="2"><path d="M18 34V16M18 16 8 4M18 16 28 4M18 16V2M18 16 4 12M18 16l14-4"/></svg></div>
  <div class="svc" style="left:871px;top:408px;width:300px"><h3>Data &amp; Fibre Installations</h3><p>Duis gravida nibh ut mauris posuere fermentum uisque sed loremlissuada mauris ut, lacinia.</p></div>
</section>

<section class="service-cards">
  <div class="card" style="left:75px">
    <div class="photo" role="img" aria-label="Electrician in safety glasses working on a commercial switchboard" style="background:linear-gradient(120deg,#3a4a66,#6b7c8c 55%,#3b4046)"></div>
    <h3>Commercial Services</h3>
    <div class="btn" style="left:167px;top:166px;width:178px;height:47px">READ MORE</div>
  </div>
  <div class="card" style="left:615px">
    <div class="photo" role="img" aria-label="Electrician fitting a ceiling cable in a home" style="background:linear-gradient(120deg,#5c5a58,#8d8b88 55%,#6a6866)"></div>
    <h3>Domestic Services</h3>
    <div class="btn" style="left:167px;top:166px;width:178px;height:47px">READ MORE</div>
  </div>
</section>

<section class="clients">
  <h2 class="section-title">Our clients</h2>
  <div class="client" style="left:75px"><i></i>Northvale</div>
  <div class="client" style="left:342px"><i></i>Brightlane</div>
  <div class="client" style="left:614px"><i></i>Ostrin</div>
  <div class="client" style="left:884px"><i></i>Calderway</div>
</section>

<section class="news">
  <h2 class="section-title" style="left:74px">Latest news</h2>
  <h2 class="section-title" style="left:706px">Testimonials</h2>

  <article class="post" style="top:117px">
    <div class="thumb" role="img" aria-label="Home theatre set-up with television and speakers" style="background:linear-gradient(135deg,#b9a58e,#3d3632)"></div>
    <h3>Cras viverra non nibh quis</h3>
    <p>Duis gravida nibh ut mauris posuere fermentum uisque sed loremlissuada mauris ut, lacinia nec elementum libero ultrices velit vitae odio euismod.</p>
  </article>
  <article class="post" style="top:304px">
    <div class="thumb" role="img" aria-label="Technician splicing fibre optic cable" style="background:linear-gradient(135deg,#4b4a4c,#2a2a2c)"></div>
    <h3>Cras viverra non nibh quis</h3>
    <p>Duis gravida nibh ut mauris posuere fermentum uisque sed loremlissuada mauris ut, lacinia nec elementum libero ultrices velit vitae odio euismod.</p>
  </article>

  <blockquote class="quote" style="top:117px">
    <div class="avatar" role="img" aria-label="Customer portrait"></div>
    <p>Duis gravida nibh ut mauris posuere fermentum uisque sed loremlissuada mauris ut, lacinia nec...”</p>
    <cite>-Name Heading</cite>
  </blockquote>
  <blockquote class="quote" style="top:304px">
    <div class="avatar" role="img" aria-label="Customer portrait"></div>
    <p>Duis gravida nibh ut mauris posuere fermentum uisque sed loremlissuada mauris ut, lacinia nec...”</p>
    <cite>-Name Heading</cite>
  </blockquote>
</section>

<section class="cta">
  <h2>Cras viverra non nibh quis varius</h2>
  <p class="sub">Duis gravida nibh ut mauris posuere fermentum uisque/</p>
  <span class="phone">1-800-555-0148</span>
  <span class="outline">CONTACT US</span>
</section>

<footer class="site-footer">
  <div class="abs footer-brand"><span class="brand-dot"></span><span class="brand-name">KORVAL</span></div>
  <p class="abs copy">Copyright © 2020. Company Name<br>All rights reserved.</p>
  <div class="abs social" aria-label="Social links"><span></span><span></span><span></span><span></span><span></span></div>

  <div class="abs fcol" style="left:342px;top:63px">
    <h4>SITE MAP</h4>
    <ul class="two"><li>Home</li><li>Blog</li><li>About Us</li><li>Clients</li><li>Services</li><li>Contact Us</li><li>Reviews</li></ul>
  </div>
  <div class="abs fcol" style="left:615px;top:63px">
    <h4>SITE MAP</h4>
    <ul class="spaced"><li>Domestic Electrical Services</li><li>Audio Visual Services</li><li>Data &amp; fibre installations</li></ul>
  </div>
  <div class="abs fcol contact" style="left:884px;top:63px">
    <h4>CONTACT INFO</h4>
    <ul>
      <li style="line-height:23px;display:block;width:190px;font-size:13.5px">412 Fernlow Road,Harwick, D07 31KT</li>
      <li><svg width="12" height="12" viewBox="0 0 24 24" fill="#222"><path d="M6.6 10.8a15 15 0 0 0 6.6 6.6l2.2-2.2c.3-.3.7-.4 1-.2 1.1.4 2.3.6 3.6.6.6 0 1 .4 1 1V20c0 .6-.4 1-1 1A17 17 0 0 1 3 4c0-.6.4-1 1-1h3.5c.6 0 1 .4 1 1 0 1.3.2 2.5.6 3.6.1.3 0 .7-.2 1z"/></svg><span style="padding-left:10px">1-800-555-0148</span></li>
      <li><svg width="13" height="11" viewBox="0 0 24 20" fill="#222"><path d="M0 2 12 10 24 2V0H0zM0 5v15h24V5l-12 8z"/></svg><span style="padding-left:9px">info@korvalworks.com.au</span></li>
    </ul>
  </div>
</footer>

</body>
</html>
```